Premium small-production winery needs a front label redesign

We produce wine from cold-climate varietal grapes, many of which were only developed in the last 50 years. Our winery, called Hollow Ridge Cellars, is housed in an industrial style building serving a premium product. We have 12 styles of wine that can accommodate a wide range of tastes. We would like to see designs that communicate old traditions (winemaking styles) blended with new ideas (newly developed grape varieties). Our ideal customer enjoys an evening that is cultured and classy, yet fun and educational. We will likely favor designs that are 4" x 4.5", but this isn't required - if we see something we love, we would consider changing the dimensions.
I've attached our current labels and 2 logo files. We are only looking for a front-label redesign. Thanks!

Target Market(s)

Our ideal customer enjoys an evening that is cultured and classy, yet fun and educational.

Font styles to use
Serif
Sans Serif
Script
Other font styles liked:
• Our current fonts are Trajan Pro, Tangerine, and Avenir.

Requirements
Must have
• We would love to see a design that could span our entire product line with only a subtle or minor change (such as printing color, or a picture) to distinguish between our 12 products. Emphasis on the part about the change should be subtle among labels.
• Some of the distinguishing characteristics of the wines:
• Color: white, orange, rosé (pink), light red, dark red
• Sweetness: dry, off-dry, semi-sweet, sweet, very sweet
• Flavors: too many to list
• Product names: 9 of the wines are named after the majority grape. The other 3 are blends of multiple grapes, with the following names: "Velvet Blush", "Opal", and "Ember".
Nice to have
• our wine list: http://hollowridgecellars.example/wine/
Should not have
• We would prefer a design that isn't too busy overall.

```html
<!DOCTYPE html>
<html lang="en">
<head>
<meta charset="utf-8">
<title>Hollow Ridge Cellars – Maréchal Foch 2013 Front Label</title>
<link rel="stylesheet" href="https://fonts.googleapis.com/css2?family=Cinzel:wght@500;600&family=Cormorant+Garamond:wght@500&family=Tangerine:wght@700&display=swap">
<style>
  :root {
    --backdrop: #a9a9a9;
    --label-black: #141414;
    --panel-white: #ffffff;
    --panel-shade: #d6d6d6;
    --text-light: #f2f2f2;
    --accent-amber: #eba012;
  }
  html, body {
    margin: 0;
    padding: 0;
    width: 801px;
    height: 1200px;
    overflow: hidden;
    background: var(--backdrop);
  }
  .canvas {
    position: relative;
    width: 801px;
    height: 1200px;
  }
  .label {
    position: absolute;
    left: 50px;
    top: 205px;
    width: 700px;
    height: 790px;
    background: var(--label-black);
    overflow: hidden;
  }
  .monogram-panel {
    position: absolute;
    left: 0;
    top: 0;
    width: 268px;
    height: 100%;
    background: linear-gradient(90deg, var(--panel-white) 0%, var(--panel-white) 50%, var(--panel-shade) 100%);
  }
  .brand-mark {
    position: absolute;
    left: 0;
    top: 0;
    width: 268px;
    height: 790px;
  }
  .brand-mark-name {
    position: absolute;
    left: 0;
    right: 0;
    top: 560px;
    margin: 0;
    text-align: center;
    font-family: "Cinzel", "Times New Roman", serif;
    font-weight: 600;
    font-size: 24px;
    letter-spacing: 1px;
    line-height: 1.25;
    color: var(--accent-amber);
  }
  .label-text {
    position: absolute;
    left: 268px;
    right: 0;
    top: 0;
    height: 100%;
    color: var(--text-light);
  }
  .winery-name {
    position: absolute;
    left: 0;
    right: 0;
    top: 292px;
    margin: 0;
    text-align: center;
    font-family: "Cinzel", "Times New Roman", serif;
    font-weight: 600;
    font-size: 42px;
    letter-spacing: 1px;
    line-height: 1;
  }
  .winery-type {
    position: absolute;
    left: 0;
    right: 0;
    top: 352px;
    margin: 0;
    text-align: center;
    font-family: "Cinzel", "Times New Roman", serif;
    font-weight: 500;
    font-size: 24px;
    letter-spacing: 6px;
    line-height: 1;
  }
  .varietal {
    position: absolute;
    left: 0;
    right: 0;
    top: 418px;
    margin: 0;
    text-align: center;
    font-family: "Tangerine", "Brush Script MT", cursive;
    font-weight: 700;
    font-size: 76px;
    color: var(--accent-amber);
    line-height: 1;
    white-space: nowrap;
  }
  .vintage {
    position: absolute;
    right: 30px;
    top: 528px;
    margin: 0;
    text-align: right;
    font-family: "Cormorant Garamond", "Times New Roman", serif;
    font-weight: 500;
    font-size: 36px;
    letter-spacing: 5px;
    font-variant-numeric: lining-nums;
    line-height: 1;
  }
</style>
</head>
<body>
  <main class="canvas">
    <section class="label">
      <div class="monogram-panel">
        <svg class="brand-mark" viewBox="0 0 268 790" aria-hidden="true">
          <circle cx="134" cy="400" r="96" fill="none" stroke="#eba012" stroke-width="14"/>
        </svg>
        <p class="brand-mark-name">HOLLOW RIDGE<br>CELLARS</p>
      </div>
      <div class="label-text">
        <h1 class="winery-name">HOLLOW RIDGE</h1>
        <p class="winery-type">CELLARS</p>
        <p class="varietal">Maréchal Foch</p>
        <p class="vintage">2013</p>
      </div>
    </section>
  </main>
</body>
</html>
```